TownDailyo - Business card + Stationery
"Discover fresh corners of your town, daily!" "Today's leading daily deals +"
TownDailyo - Business card + Stationery - Information Technology
Creative Brief
Use specific fonts
Font used is good but open to new ideas
Bright & Fun-filled
Marcus Delwyn
Creator + Director
marcus@towndailyo.example
towndailyo.example
I am looking for a modern catchy design for a new set of business cards. Looking for stationery such as: email template - small logo with web link - Post card - Note pad etc... Looking for a modern design that contains the web link and text to match business card theme. Open to new ideas. Chatterbook and Chirplet logo "TOWNDAILYO" can be used on the cards too. I will make further comments as the various designs come in.
Logo + www. << >>.com on either side of the logo Text at bottom Discover fresh corners of your town, daily

```html
<!DOCTYPE html>
<html lang="en">
<head>
<meta charset="utf-8">
<title>TownDailyo — Business Card + Stationery</title>
<link href="https://fonts.googleapis.com/css2?family=Open+Sans:wght@400;600;700&display=swap" rel="stylesheet">
<style>
:root{
  --bg-top:#ffffff;
  --bg-bottom:#dcdcdc;
  --bar:#1e1e1e;
  --paper:#ffffff;
  --blue:#1a7fd0;
  --blue-dark:#0f5fa6;
  --orange:#f39a1e;
  --ink:#4a4a4a;
  --muted:#8a8a8a;
  --shadow:0 2px 5px rgba(0,0,0,.28);
}
*{box-sizing:border-box;margin:0;padding:0}
html,body{width:1200px;height:444px;overflow:hidden}
body{font-family:"Open Sans",Arial,sans-serif;color:var(--ink);
  background:linear-gradient(var(--bg-top),var(--bg-bottom));position:relative}
.top-bar{position:absolute;left:0;top:0;width:1200px;height:22px;background:var(--bar)}
.piece{position:absolute;background:var(--paper);box-shadow:var(--shadow);overflow:hidden}
.label{position:absolute;font-size:6px;color:var(--muted);text-align:center;width:100%;bottom:-10px}
.holder{position:absolute}
.logo-art{position:absolute;border-radius:40% 40% 20% 20%;
  background:radial-gradient(circle at 50% 35%,#f6c243 0 18%,#e4508f 19% 34%,#46b6e6 35% 55%,#2c6fb8 56% 100%)}
.wave{position:absolute;left:0;bottom:0;width:100%}
.name{font-weight:700;color:var(--blue);font-size:9px}
.small{font-size:5px;line-height:8px;color:var(--ink)}
.footer-text{position:absolute;left:0;width:100%;text-align:center;color:#fff;font-size:4.5px}
.tagline{font-size:6px;font-weight:600;color:var(--orange);text-align:center;position:absolute;width:100%}
.icon{display:inline-block;width:4px;height:4px;background:var(--blue);border-radius:50%;margin-right:3px;vertical-align:middle}
.flap{position:absolute;left:0;top:0;width:100%;height:100%}
</style>
</head>
<body>
<div class="top-bar"></div>

<!-- Business card front -->
<div class="holder" style="left:24px;top:84px;width:173px;height:101px">
  <div class="piece" style="inset:0">
    <div class="logo-art" role="img" aria-label="TownDailyo colourful town illustration" style="left:10px;top:14px;width:42px;height:44px"></div>
    <div style="position:absolute;left:66px;top:14px">
      <div class="name">Marcus Delwyn</div>
      <div class="small">Creator + Director</div>
      <div class="small" style="color:var(--blue)">marcus@towndailyo.example</div>
      <div class="small" style="margin-top:4px"><span class="icon"></span>+1 555 0142</div>
      <div class="small"><span class="icon"></span>towndailyo.example</div>
    </div>
    <svg class="wave" viewBox="0 0 300 40" preserveAspectRatio="none" height="22">
      <path d="M0 22 Q150 2 300 18 L300 40 L0 40Z" fill="var(--blue)"/>
      <path d="M0 16 Q150 -4 300 12" stroke="var(--orange)" stroke-width="3" fill="none"/>
    </svg>
  </div>
  <div class="label">Front Card</div>
</div>

<!-- Business card back white -->
<div class="holder" style="left:24px;top:197px;width:173px;height:96px">
  <div class="piece" style="inset:0">
    <div class="logo-art" role="img" aria-label="TownDailyo colourful town illustration" style="left:28px;top:10px;width:42px;height:46px"></div>
    <div class="name" style="position:absolute;left:76px;top:34px">TownDailyo</div>
    <div class="tagline" style="top:64px">Discover fresh corners of your town, daily!</div>
    <svg class="wave" viewBox="0 0 300 40" preserveAspectRatio="none" height="18">
      <path d="M0 22 Q150 2 300 18 L300 40 L0 40Z" fill="var(--blue)"/>
      <path d="M0 16 Q150 -4 300 12" stroke="var(--orange)" stroke-width="3" fill="none"/>
    </svg>
  </div>
  <div class="label">Back Card White</div>
</div>

<!-- Business card back blue -->
<div class="holder" style="left:24px;top:302px;width:173px;height:101px">
  <div class="piece" style="inset:0;background:linear-gradient(var(--blue),var(--blue-dark))">
    <div class="logo-art" role="img" aria-label="TownDailyo colourful town illustration" style="left:22px;top:18px;width:44px;height:48px"></div>
    <div style="position:absolute;left:76px;top:30px;color:#fff">
      <div class="name" style="color:#fff">TownDailyo</div>
      <div class="small" style="color:#fff">towndailyo.example</div>
    </div>
    <div class="tagline" style="top:80px;color:#fff">Discover fresh corners of your town, daily!</div>
  </div>
  <div class="label">Back Card Blue</div>
</div>

<!-- Letterhead page 1 -->
<div class="holder" style="left:216px;top:29px;width:300px;height:396px">
  <div class="piece" style="inset:0">
    <div class="logo-art" role="img" aria-label="TownDailyo colourful town illustration" style="left:70px;top:14px;width:46px;height:50px"></div>
    <div style="position:absolute;left:124px;top:18px">
      <div class="small"><span class="icon"></span>+1 555 0142</div>
      <div class="small"><span class="icon"></span>marcus@towndailyo.example</div>
      <div class="small"><span class="icon"></span>towndailyo.example</div>
    </div>
    <svg class="wave" viewBox="0 0 300 40" preserveAspectRatio="none" height="30">
      <path d="M0 22 Q150 2 300 18 L300 40 L0 40Z" fill="var(--blue)"/>
      <path d="M0 16 Q150 -4 300 12" stroke="var(--orange)" stroke-width="3" fill="none"/>
    </svg>
    <div class="footer-text" style="bottom:6px">towndailyo.example &nbsp;|&nbsp; marcus@towndailyo.example &nbsp;|&nbsp; +1 555 0142</div>
  </div>
  <div class="label">Letterhead Page 1</div>
</div>

<!-- Letterhead page 2 -->
<div class="holder" style="left:528px;top:29px;width:300px;height:396px">
  <div class="piece" style="inset:0">
    <div class="logo-art" role="img" aria-label="TownDailyo colourful town illustration" style="left:24px;top:14px;width:46px;height:50px"></div>
    <svg class="wave" viewBox="0 0 300 40" preserveAspectRatio="none" height="30">
      <path d="M0 22 Q150 2 300 18 L300 40 L0 40Z" fill="var(--blue)"/>
      <path d="M0 16 Q150 -4 300 12" stroke="var(--orange)" stroke-width="3" fill="none"/>
    </svg>
    <div class="footer-text" style="bottom:6px">towndailyo.example &nbsp;|&nbsp; marcus@towndailyo.example &nbsp;|&nbsp; +1 555 0142</div>
  </div>
  <div class="label">Letterhead Page 2</div>
</div>

<!-- Envelope back -->
<div class="holder" style="left:845px;top:101px;width:331px;height:144px">
  <div class="piece" style="inset:0">
    <svg class="flap" viewBox="0 0 331 144" preserveAspectRatio="none">
      <path d="M0 0 L165 80 L331 0" stroke="#cfcfcf" stroke-width="1" fill="#f7f7f7"/>
      <path d="M0 144 L130 70 M331 144 L200 70" stroke="#dedede" stroke-width="1" fill="none"/>
    </svg>
    <div class="logo-art" role="img" aria-label="TownDailyo colourful town illustration" style="left:143px;top:30px;width:44px;height:44px"></div>
    <div class="small" style="position:absolute;left:0;width:100%;top:80px;text-align:center;color:var(--blue)">towndailyo.example</div>
  </div>
  <div class="label">Envelope Back</div>
</div>

<!-- Envelope front -->
<div class="holder" style="left:845px;top:283px;width:331px;height:125px">
  <div class="piece" style="inset:0">
    <div class="logo-art" role="img" aria-label="TownDailyo colourful town illustration" style="left:12px;top:10px;width:44px;height:46px"></div>
    <div class="small" style="position:absolute;left:62px;top:40px;color:var(--blue)">towndailyo.example</div>
    <svg class="wave" viewBox="0 0 300 40" preserveAspectRatio="none" height="24">
      <path d="M0 22 Q150 2 300 18 L300 40 L0 40Z" fill="var(--blue)"/>
      <path d="M0 16 Q150 -4 300 12" stroke="var(--orange)" stroke-width="3" fill="none"/>
    </svg>
  </div>
  <div class="label">Envelope Front</div>
</div>
</body>
</html>
```